Media and Film Company Needs a New Website

We produce highly stylized commercials and film pieces for our clients. We also produce live events, both corporate and theatrical. Looking for a site that can show off our client videos - have a polished way to show off our team, and be able to create pages to highlight our clients and give a full overview of our project/process with them. We design simple website for some of our clients - so we are very wordpress familiar, and would like something that doesn't feel like a template.

Target Market(s)

content creators, creative directors, production teams, marketing agencies

Industry/Entity Type

Film Production

Number of Pages Required

4 page

Font styles to use
Sans Serif

Requirements
Must have
• slick looking video embed (from YT or Vimeo)
• project pages - client snapshot (what we did for them, how we did it)
• nice landing page, have our company video reel on the page
• testimonials
• contact page
• ability to have photos as a background if we want
Nice to have
• polished clean look - look to our logo colors and linear elements
• we produce very stylized videos for our clients and our website should reflect that
Should not have
• template look or feel to it- please bring your flare to the project!
• take a look at our current site - brelvostudio.com we need a better way to highlight our work and our clients

```html
<!DOCTYPE html>
<html lang="en">
<head>
<meta charset="utf-8">
<title>Brelvo Studio — Portfolio</title>
<link href="https://fonts.googleapis.com/css2?family=Montserrat:wght@400;500;600;700&display=swap" rel="stylesheet">
<style>
:root{
  --page:#252525;
  --ink:#3a3a3a;
  --muted:#a9a9a9;
  --white:#ffffff;
  --panel:#f1f2f4;
  --field:#ebebeb;
  --cyan:#12b5ea;
  --blue:#0a63f5;
  --red:#e0262b;
  --line:#dcdcdc;
}
*{box-sizing:border-box;margin:0;padding:0}
html,body{width:684px;height:1200px;overflow:hidden}
body{background:var(--page);font-family:"Montserrat",sans-serif;color:var(--ink);position:relative}
.abs{position:absolute}

/* header */
.brand{left:43px;top:13px;color:var(--white);font-weight:700;font-size:11px;letter-spacing:.5px;display:flex;align-items:center;gap:5px}
.brand-dot{width:7px;height:7px;border-radius:50%;background:var(--cyan)}
.nav{top:15px;left:0;width:684px;height:24px}
.nav a{position:absolute;color:var(--white);font-size:7px;text-decoration:none;letter-spacing:.2px}
.nav a.active{color:var(--cyan)}
.nav-underline{left:221px;top:31px;width:47px;height:4px;background:var(--cyan)}

/* video */
.video{left:90px;top:54px;width:504px;height:312px;background:linear-gradient(180deg,#6f8f95 0%,#9aa7a0 40%,#6b6a5c 75%,#4a4a40 100%)}
.progress{left:90px;top:340px;width:504px;height:4px;background:#555}
.progress-played{left:90px;top:340px;width:383px;height:4px;background:var(--red)}
.progress-buffer{left:473px;top:340px;width:31px;height:4px;background:#cfcfcf}
.progress-knob{left:467px;top:336px;width:12px;height:12px;border-radius:50%;background:var(--white);border:3px solid var(--red)}
.controls{left:90px;top:346px;width:504px;height:20px}
.time{left:201px;top:351px;color:#ccc;font-size:6.5px}
.time b{color:var(--white)}

/* content panel */
.panel{left:36px;top:385px;width:612px;height:768px;background:var(--white)}
.sidebar{left:439px;top:385px;width:209px;height:768px;background:var(--panel)}
.label{font-size:7px;letter-spacing:.4px;color:var(--ink)}
.about-text{left:89px;top:424px;width:320px;font-size:6.3px;line-height:8px;color:#555}
.divider{left:36px;top:480px;width:403px;height:1px;background:var(--line)}
.field{left:89px;width:218px;background:var(--field);font-size:6.5px;color:#8a8a8a;padding:8px 10px}
.post-btn{left:89px;top:656px;width:218px;height:23px;background:linear-gradient(90deg,var(--cyan),var(--blue));color:var(--white);font-weight:700;font-size:8.5px;display:flex;align-items:center;justify-content:center}

.comment{width:270px}
.avatar{position:absolute;left:0;top:0;width:20px;height:20px;border-radius:50%}
.c-body{margin-left:28px}
.c-name{font-size:5.8px;font-weight:700;color:#222}
.c-time{font-weight:400;color:#c2c2c2;font-size:4.6px;margin-left:4px}
.c-text{font-size:5.8px;line-height:10.5px;color:#333;margin-top:1px}
.c-text .mention{color:var(--cyan);font-weight:600}
.c-actions{font-size:4.6px;color:#b0b0b0;margin-top:2px;letter-spacing:.2px}
.c-actions b{color:#222}
.load-more{left:119px;top:1097px;width:253px;height:28px;border:1px solid var(--line);font-size:4.8px;letter-spacing:.6px;color:#aaa;display:flex;align-items:center;justify-content:center}

/* up next */
.upnext-title{left:448px;top:399px;font-size:7px;color:#222}
.autoplay{left:526px;top:399px;font-size:7px;color:#444}
.toggle{left:573px;top:395px;width:22px;height:13px;border-radius:7px;background:#9fdcf4}
.toggle::after{content:"";position:absolute;right:0;top:0;width:13px;height:13px;border-radius:50%;background:var(--cyan)}
.thumb{left:492px;width:103px;height:75px;background:linear-gradient(135deg,#8d6a4c 0%,#c9a07a 45%,#d7a0d8 100%)}
.thumb.green{background:linear-gradient(180deg,#a9c7e4 0%,#c9d9c8 45%,#6a9a43 100%)}
.thumb.meadow{background:linear-gradient(135deg,#6c5440 0%,#9b7a55 45%,#7fa14c 100%)}
.play{position:absolute;left:35px;top:21px;width:32px;height:32px;border-radius:50%;background:rgba(30,30,30,.85)}
.play::after{content:"";position:absolute;left:12px;top:9px;border-left:11px solid #fff;border-top:7px solid transparent;border-bottom:7px solid transparent}
.thumb-title{left:492px;width:110px;font-size:6.5px;line-height:8px;letter-spacing:.3px;color:#555}
.thumb-meta{left:492px;font-size:4.6px;color:#666}

/* footer */
.copyright{left:35px;top:1170px;font-size:6.8px;color:var(--white);letter-spacing:.2px}
.social{top:1165px;width:18px;height:18px;border-radius:50%;background:#2d6fb0;border:1.5px solid #e8e8e8}
</style>
</head>
<body>

<header>
  <div class="abs brand"><span class="brand-dot"></span>BRELVO STUDIO</div>
  <nav class="abs nav">
    <a style="left:169px">HOME</a>
    <a class="active" style="left:223px">PORTFOLIO</a>
    <a style="left:288px">ABOUT US</a>
    <a style="left:342px">TESTIMONIALS</a>
    <a style="left:421px">PRESS</a>
    <a style="left:478px">CONTACT</a>
  </nav>
  <div class="abs nav-underline"></div>
</header>

<main>
  <div class="abs video" role="img" aria-label="Video frame: skateboarder jumping stairs at a palm-lined skate park"></div>
  <div class="abs progress"></div>
  <div class="abs progress-played"></div>
  <div class="abs progress-buffer"></div>
  <div class="abs progress-knob"></div>
  <svg class="abs controls" viewBox="0 0 504 20" width="504" height="20">
    <rect x="10" y="5" width="2.5" height="8" fill="#fff"/><rect x="15" y="5" width="2.5" height="8" fill="#fff"/>
    <path d="M34 7h3l4-3v11l-4-3h-3z" fill="#fff"/>
    <rect x="46" y="8.5" width="60" height="1.5" fill="#fff"/>
    <circle cx="84" cy="9" r="4.5" fill="#fff"/>
    <circle cx="470" cy="9" r="4.5" fill="none" stroke="#fff" stroke-width="1.3"/><path d="M470 6.5v3h2" stroke="#fff" stroke-width="1.2" fill="none"/>
    <circle cx="489" cy="9" r="3.5" fill="none" stroke="#fff" stroke-width="2.2" stroke-dasharray="2 1.5"/>
    <path d="M506 4h-4M506 4v4M506 14v-4M506 14h-4M584 0" stroke="#fff" fill="none"/>
    <path d="M502 5h4v4M502 14h4v-4M493 0" stroke="none"/>
    <path d="M498 4h-3v3M498 14h-3v-3M507 4h3v3M507 14h3v-3" transform="translate(-9 0)" stroke="#fff" stroke-width="1.3" fill="none"/>
  </svg>
  <div class="abs time">3:21 / <b>4:45</b></div>

  <section class="abs panel"></section>
  <aside class="abs sidebar"></aside>

  <div class="abs label" style="left:89px;top:400px">ABOUT</div>
  <p class="abs about-text">Quillfork chose Brelvo Studio to help tell the story of the events team at Lantern Hall. We spent 4 days with them to capture time-lapse footage for 3 different events, as well as full motion video of their performance and event spaces.</p>
  <div class="abs divider"></div>

  <div class="abs label" style="left:88px;top:493px">COMMENTS &nbsp; 26</div>
  <div class="abs field" style="top:509px;height:22px">Your name</div>
  <div class="abs field" style="top:539px;height:22px">Email address</div>
  <div class="abs field" style="top:572px;height:73px">Add a comment here...</div>
  <div class="abs post-btn">Post Comment</div>

  <div class="abs comment" style="left:95px;top:716px">
    <span class="avatar" style="background:#111"></span>
    <div class="c-body">
      <div class="c-name">Dorian<span class="c-time">• &nbsp;9 hours ago</span></div>
      <div class="c-text">Fascinating!! Brilliant work Matteo!! I'll see later again, more than once, it's full of details and talent touches!</div>
      <div class="c-actions">↰ REPLY &nbsp;• &nbsp;<b>▲ LIKE 13</b></div>
    </div>
  </div>
  <div class="abs" style="left:129px;top:762px;width:1px;height:30px;background:#ddd"></div>
  <div class="abs comment" style="left:132px;top:766px;width:240px">
    <span class="avatar" style="background:#1a1a1a;width:17px;height:17px"></span>
    <div class="c-body" style="margin-left:24px">
      <div class="c-name">Rowan Pell<span class="c-time">• &nbsp;5 days ago</span></div>
      <div class="c-text">Awesome as always. travel to Vietnam please</div>
      <div class="c-actions">↰ REPLY &nbsp;• &nbsp;△ LIKE</div>
    </div>
  </div>

  <div class="abs comment" style="left:95px;top:820px">
    <span class="avatar" style="background:#e85b2c"></span>
    <div class="c-body">
      <div class="c-name">Marisol Vance<span class="c-time">• &nbsp;10 days ago</span></div>
      <div class="c-text">Love em, site really great too! Personally would have gone right with <span class="mention">@Teo Brandt</span><br>It's just so clean!</div>
      <div class="c-actions">↰ REPLY &nbsp;• &nbsp;△ LIKE</div>
    </div>
  </div>

  <div class="abs comment" style="left:95px;top:884px">
    <span class="avatar" style="background:var(--red)"></span>
    <div class="c-body">
      <div class="c-name">Lukas Ferrin<span class="c-time">• &nbsp;20 days ago</span></div>
      <div class="c-text">This video is a visual buffet! You're one of my greatest inspirations in filmmaking and a reason why I continue to pursue it as a passion and career today, despite how tiring it can be. Drains us in one way, fulfils us in another. Kudos to your work, I'm looking forward to the next one!</div>
      <div class="c-actions">↰ REPLY &nbsp;• &nbsp;△ LIKE 4</div>
    </div>
  </div>

  <div class="abs comment" style="left:95px;top:969px">
    <span class="avatar" style="background:#3a2222"></span>
    <div class="c-body">
      <div class="c-name">Nadia Oslo<span class="c-time">• &nbsp;1 month ago</span></div>
      <div class="c-text">One of the coolest edit I have seen with timelapses! Such a play with velocity. Usually people just stack one beautiful take to another :) And nice shot stuff. Great work.</div>
      <div class="c-actions">↰ REPLY &nbsp;• &nbsp;<b>▲ LIKE 2</b></div>
    </div>
  </div>

  <div class="abs comment" style="left:95px;top:1033px">
    <span class="avatar" style="background:linear-gradient(135deg,#e33 0%,#fc3 35%,#3c6 60%,#36f 100%)"></span>
    <div class="c-body">
      <div class="c-name">Henrik Dalby<span class="c-time">• &nbsp;1 month ago</span></div>
      <div class="c-text">I think if I watch this every day for a month I will automatically become a better editor :)<br>Simply mind blowing!</div>
      <div class="c-actions">↰ REPLY &nbsp;• &nbsp;△ LIKE</div>
    </div>
  </div>

  <div class="abs load-more">LOAD MORE COMMENTS</div>

  <div class="abs upnext-title">Up Next</div>
  <div class="abs autoplay">Autoplay</div>
  <div class="abs toggle"></div>

  <div class="abs thumb" style="top:418px" role="img" aria-label="Video thumbnail: animated short, animal scene"><span class="play"></span></div>
  <div class="abs thumb-title" style="top:498px">EVENTS AT THE HARLOW CENTER | LANTERN HALL</div>
  <div class="abs thumb-meta" style="top:517px">Quillfork. 3K views. 3 Hours ago</div>

  <div class="abs thumb green" style="top:547px" role="img" aria-label="Video thumbnail: animated short, meadow scene"><span class="play"></span></div>
  <div class="abs thumb-title" style="top:627px">EVENTS AT THE HARLOW CENTER | LANTERN HALL</div>
  <div class="abs thumb-meta" style="top:646px">Quillfork. 3K views. 3 Hours ago</div>

  <div class="abs thumb meadow" style="top:675px" role="img" aria-label="Video thumbnail: animated short, forest scene"><span class="play"></span></div>
  <div class="abs thumb-title" style="top:755px">EVENTS AT THE HARLOW CENTER | LANTERN HALL</div>
  <div class="abs thumb-meta" style="top:774px">Quillfork. 3K views. 3 Hours ago</div>

  <div class="abs thumb" style="top:804px" role="img" aria-label="Video thumbnail: animated short, animal scene"><span class="play"></span></div>
  <div class="abs thumb-title" style="top:884px">EVENTS AT THE HARLOW CENTER | LANTERN HALL</div>
  <div class="abs thumb-meta" style="top:903px">Quillfork. 3K views. 3 Hours ago</div>
</main>

<footer>
  <div class="abs copyright">©2016 BRELVO STUDIO</div>
  <span class="abs social" style="left:523px" aria-label="Social link"></span>
  <span class="abs social" style="left:550px;background:#2aa3d8" aria-label="Social link"></span>
  <span class="abs social" style="left:577px;background:#c4232b" aria-label="Social link"></span>
  <span class="abs social" style="left:603px;background:#1ab7b5" aria-label="Social link"></span>
  <span class="abs social" style="left:630px;background:#1e88c9" aria-label="Social link"></span>
</footer>

</body>
</html>
```